QM Kalorvex.Brendal GmbH needed a letterhead template

For English scroll down. We need a letterhead template and since we already have our logo design successfully with you, we now want to also design the letterhead with you. Down in the uploaded file you see what is important and what should definitely be seen on our template. The template should be like the homepage (www.kalorvex.brendal) held in red, blue and white. We need a letter-head submission. In the bottom in the chapter "databases uploading" you can find the most important things, did must be on the submission. The submission shoulderstand be in the colors blue, red and white like our homepage (www.kalorvex.brendal).

```html
<!DOCTYPE html>
<html lang="de">
<head>
<meta charset="utf-8">
<title>QM Kalorvex.Brendal GmbH – Briefpapier</title>
<link href="https://fonts.googleapis.com/css2?family=Open+Sans:wght@400;600;700&display=swap" rel="stylesheet">
<style>
  :root {
    --brand-red: #c8202b;
    --brand-blue: #3b73ab;
    --paper: #ffffff;
    --ink: #1e1e1e;
    --backdrop: #d6d6d6;
  }
  * { box-sizing: border-box; margin: 0; padding: 0; }
  html, body { width: 1200px; height: 790px; overflow: hidden; }
  body {
    background: var(--backdrop);
    font-family: "Open Sans", Arial, sans-serif;
    color: var(--ink);
    position: relative;
  }
  .letterhead {
    position: absolute;
    left: 330px; top: 13px;
    width: 540px; height: 764px;
    background: var(--paper);
    overflow: hidden;
  }
  .brand {
    position: absolute;
    left: 44px; top: 40px;
    display: flex; align-items: center; gap: 8px;
  }
  .brand-mark {
    width: 14px; height: 14px; border-radius: 50%;
    background: var(--brand-red);
  }
  .brand-name {
    font-size: 24px; font-weight: 700;
    color: var(--brand-blue);
    letter-spacing: 0.2px;
  }
  .sender {
    position: absolute;
    right: 34px; top: 42px;
    width: 150px;
    border-left: 1.5px solid var(--brand-red);
    padding-left: 10px;
    font-size: 7px; line-height: 1.35;
    font-style: normal;
  }
  .footer-bar {
    position: absolute;
    left: 0; top: 622px;
    width: 12px; height: 62px;
    background: var(--brand-red);
  }
  .contact {
    position: absolute;
    left: 40px; top: 624px;
    list-style: none;
    font-size: 9.5px; line-height: 1.45;
  }
  .contact li { display: flex; align-items: center; gap: 9px; }
  .contact svg { width: 8px; height: 8px; fill: var(--brand-blue); flex: none; }
  .bank {
    position: absolute;
    left: 296px; top: 650px;
    font-size: 9.5px; line-height: 1.45;
  }
  .footer-wave {
    position: absolute;
    left: 0; bottom: 0;
    width: 540px; height: 200px;
  }
</style>
</head>
<body>
  <main class="letterhead">
    <header class="brand">
      <span class="brand-mark"></span>
      <span class="brand-name">Kalorvex.Brendal</span>
    </header>

    <address class="sender">
      Geschäftsführer Dr. Holvik Marten<br>
      Lindweg 12<br>
      4821 Orsbach, Veldra<br>
      Österreich
    </address>

    <svg class="footer-wave" viewBox="0 0 540 200" aria-hidden="true">
      <path d="M340 200 Q470 170 540 40 L540 200 Z" fill="var(--brand-blue)"/>
      <path d="M300 200 Q445 176 512 72 Q455 168 332 200 Z" fill="var(--brand-red)"/>
    </svg>

    <div class="footer-bar"></div>

    <ul class="contact">
      <li><svg viewBox="0 0 10 10"><path d="M5 0a3.5 3.5 0 0 0-3.5 3.5C1.5 6 5 10 5 10s3.5-4 3.5-6.5A3.5 3.5 0 0 0 5 0zm0 5a1.4 1.4 0 1 1 0-2.8A1.4 1.4 0 0 1 5 5z"/></svg>QM Kalorvex.Brendal GmbH , Lindweg 12, 4821 Orsbach, Veldra Österreich</li>
      <li><svg viewBox="0 0 10 10"><path d="M1 2h8v2H1zM2 4.5h6l1 4.5H1z"/></svg>0800 XX XX XX</li>
      <li><svg viewBox="0 0 10 10"><path d="M0 2h10v6H0zM1 3l4 3 4-3v-.5H1z" fill-rule="evenodd"/></svg>contact@kalorvex.brendal</li>
      <li><svg viewBox="0 0 10 10"><circle cx="5" cy="5" r="4.5"/></svg>www.kalorvex.brendal</li>
    </ul>

    <div class="bank">
      Brennbank XXXX<br>
      IBAN: ATXX XXXX XXXX XXXX<br>
      BIC: XXXX<br>
      UID-Nr.: ATUXXXXX
    </div>
  </main>
</body>
</html>
```